Security Company Business Card
Iron Vale
Project: Security Company Business Card
Security Company Business Card - Security
Creative Brief
Professional
Helena Brisco
Managing Director
5182 Loxley Terrace Naples, Florida USA
hbrisco@ivxsecurity.example
Be creative, new look, simple but powerful. Would like the uploaded IVX logo on the front with Iron Vale Security upload on rear
Iron Vale Security up load on the rear, but am open to creative design other than up load.
brisco7290 brisco7290
Hello Designers: Our team is looking for designs using both black/gold and red/white uploads. We are looking for something different possible a two dimension or faded look highlighting the logo to names of employees. Please show logo on rear and other opion the wording upload "Iron Vale" -Security- on the rear of card. Would like to different styles. Its importand the names on cards are clear and stand out. You need not add a web site address we will be using only email address for cards. Regards, IVX Team

```html
<!DOCTYPE html>
<html lang="en">
<head>
<meta charset="utf-8">
<title>Iron Vale Security – Business Card</title>
<link href="https://fonts.googleapis.com/css2?family=Montserrat:wght@400;600;700&family=Open+Sans:wght@400;600&display=swap" rel="stylesheet">
<style>
  :root{
    --stage:#cfc6b8;
    --card:#0b0b0b;
    --card-edge:#1c1c1c;
    --gold-light:#f2e23a;
    --gold:#d9c21a;
    --gold-dark:#8f7c08;
    --white:#ffffff;
    --muted:#c9c9c9;
    --strip:#8a8a8a;
    --silver-light:#f1f1f1;
    --silver-dark:#9a9a9a;
  }
  *{margin:0;padding:0;box-sizing:border-box}
  html,body{width:1200px;height:969px;overflow:hidden}
  body{background:var(--stage);position:relative;font-family:"Open Sans",sans-serif}

  .card{
    position:absolute;top:152px;width:380px;height:665px;
    background:var(--card);border:1px solid var(--card-edge);
    box-shadow:0 12px 30px rgba(0,0,0,.35);overflow:hidden;
  }
  .card-back{left:170px}
  .card-front{left:650px}

  /* back */
  .web-bar{
    position:absolute;left:38px;top:372px;width:230px;height:44px;
    background:linear-gradient(180deg,var(--gold-light),var(--gold) 55%,var(--gold-dark));
    display:flex;align-items:center;justify-content:center;
    font-family:"Montserrat",sans-serif;font-size:15px;color:#3a3200;letter-spacing:.2px;
  }

  /* front */
  .brand{position:absolute;left:0;top:58px;width:100%;text-align:center;color:var(--white)}
  .brand-mark{width:96px;height:96px;margin:0 auto 14px;border:6px solid var(--white);border-radius:50%}
  .brand-name{font-family:"Montserrat",sans-serif;font-weight:700;font-size:30px;letter-spacing:1px;line-height:1.15;text-transform:uppercase}

  .identity{position:absolute;left:0;top:288px;width:100%;height:52px}
  .identity-bar{
    position:absolute;left:0;top:0;width:112px;height:52px;
    background:linear-gradient(180deg,var(--gold-light),var(--gold) 55%,var(--gold-dark));
  }
  .identity-text{position:absolute;left:132px;top:2px;color:var(--white)}
  .person-name{font-family:"Montserrat",sans-serif;font-weight:600;font-size:20px;letter-spacing:.5px;text-transform:uppercase}
  .person-role{font-size:14px;color:var(--muted)}

  .contact-strip{
    position:absolute;left:0;top:400px;width:46px;height:230px;
    background:linear-gradient(90deg,#6f6f6f,var(--strip));
  }
  .contact-list{position:absolute;left:0;top:410px;list-style:none;width:100%}
  .contact-list li{display:flex;align-items:center;height:34px}
  .contact-list .icon{width:46px;display:flex;justify-content:center}
  .contact-list svg{width:16px;height:16px;fill:var(--white)}
  .contact-list span{padding-left:28px;font-size:13.5px;color:var(--white);letter-spacing:.2px}

  .base-band{
    position:absolute;left:0;bottom:0;width:100%;height:34px;
    background:linear-gradient(180deg,var(--silver-light),var(--silver-dark));
  }
</style>
</head>
<body>

  <section class="card card-back" aria-label="Card back">
    <div class="web-bar">www.ironvale.example</div>
  </section>

  <section class="card card-front" aria-label="Card front">
    <header class="brand">
      <div class="brand-mark"></div>
      <div class="brand-name">Iron Vale<br>Security</div>
    </header>

    <div class="identity">
      <div class="identity-bar"></div>
      <div class="identity-text">
        <div class="person-name">Helena Brisco</div>
        <div class="person-role">Managing Director</div>
      </div>
    </div>

    <div class="contact-strip"></div>
    <ul class="contact-list">
      <li><div class="icon"><svg viewBox="0 0 24 24"><path d="M6.6 10.8a15 15 0 0 0 6.6 6.6l2.2-2.2a1 1 0 0 1 1-.25 11.4 11.4 0 0 0 3.6.57 1 1 0 0 1 1 1V20a1 1 0 0 1-1 1A17 17 0 0 1 3 4a1 1 0 0 1 1-1h3.5a1 1 0 0 1 1 1c0 1.25.2 2.45.57 3.57a1 1 0 0 1-.25 1z"/></svg></div><span>555 014 2290</span></li>
      <li><div class="icon"><svg viewBox="0 0 24 24"><rect x="6" y="2" width="12" height="20" rx="2"/><rect x="8" y="4" width="8" height="13" fill="#777"/></svg></div><span>555 014 2291</span></li>
      <li><div class="icon"><svg viewBox="0 0 24 24"><rect x="3" y="6" width="18" height="14" rx="1"/><rect x="6" y="2" width="12" height="6" fill="#777"/></svg></div><span>555 014 2292</span></li>
      <li><div class="icon"><svg viewBox="0 0 24 24"><path d="M2 5h20v14H2z"/><path d="M2 5l10 8 10-8" fill="none" stroke="#777" stroke-width="2"/></svg></div><span>hbrisco@ivxsecurity.example</span></li>
      <li><div class="icon"><svg viewBox="0 0 24 24"><circle cx="12" cy="12" r="10"/><path d="M2 12h20M12 2c3 3 3 17 0 20M12 2c-3 3-3 17 0 20" fill="none" stroke="#777" stroke-width="1.5"/></svg></div><span>www.ironvale.example</span></li>
      <li><div class="icon"><svg viewBox="0 0 24 24"><path d="M12 2a7 7 0 0 0-7 7c0 5 7 13 7 13s7-8 7-13a7 7 0 0 0-7-7zm0 9.5A2.5 2.5 0 1 1 12 6.5a2.5 2.5 0 0 1 0 5z"/></svg></div><span>5182 Loxley Terrace Naples, FL</span></li>
    </ul>

    <div class="base-band"></div>
  </section>

</body>
</html>
```